Concrete Grinding and Polishing company business card with logo, based in Australia.

We need a business card design along with logo for a new company based in Melbourne called BrightLap. We specialise in the grinding and polishing of concrete. Polished concrete is durable, easy to maintain, cost effective, dust proof, has increased light reflectivity, and is slip resistant, among other benefits. In short, polished concrete is a popular flooring solution because of its practical advantages, as well as it's decorative appeal.

Industry/Entity Type

Business

Requirements
Must have
• It must have the company name(BrightLap) as well as the slogan: A Cut Above The Rest.
Nice to have
• Something that symbolises polished concrete. Would also like it to have a silver background with black writing, if possible.

```html
<!DOCTYPE html>
<html lang="en">
<head>
<meta charset="utf-8">
<title>BrightLap Business Card</title>
<link rel="stylesheet" href="https://fonts.googleapis.com/css2?family=Questrial&family=Josefin+Sans:wght@600;700&display=swap">
<style>
  :root{
    --stage:#2c2a1a;
    --glow:rgba(240,236,210,.75);
    --band:#050505;
    --terrazzo-a:#5f6068;
    --terrazzo-b:#8d8e97;
    --floor-light:#d2d4d6;
    --floor-mid:#a9acae;
    --floor-warm:#b99a4e;
    --name-grey:#b4b4b4;
    --ink:#0a0a0a;
    --label:#f2f2f2;
    --panel:rgba(10,10,10,.82);
    --panel-text:#d9d9d9;
    --mark:#2a2420;
  }
  *{margin:0;padding:0;box-sizing:border-box}
  html,body{width:1200px;height:686px;overflow:hidden;background:var(--stage)}
  .stage{position:relative;width:1200px;height:686px}
  .card{position:absolute;width:644px;height:384px;overflow:hidden;box-shadow:0 0 10px 3px var(--glow)}
  .card--front{left:46px;top:25px}
  .card--back{left:529px;top:245px}
  .terrazzo{position:absolute;left:0;width:100%;background:linear-gradient(90deg,var(--terrazzo-a),var(--terrazzo-b) 40%,var(--terrazzo-a) 70%,var(--terrazzo-b))}
  .terrazzo--top{top:0;height:41px}
  .terrazzo--bottom{bottom:0;height:32px}
  .floor{position:absolute;left:0;top:41px;width:100%;height:311px;
    background:
      radial-gradient(ellipse 230px 150px at 72% 50%,rgba(185,154,78,.85),rgba(185,154,78,0) 100%),
      linear-gradient(160deg,var(--floor-mid),var(--floor-light) 45%,var(--floor-mid))}
  .card--back .floor{background:
      radial-gradient(ellipse 230px 150px at 20% 60%,rgba(185,154,78,.85),rgba(185,154,78,0) 100%),
      linear-gradient(160deg,var(--floor-mid),var(--floor-light) 45%,var(--floor-mid))}
  .band{position:absolute;left:0;width:100%;background:var(--band)}
  .band--top{top:41px;height:25px}
  .band--bottom{top:325px;height:27px}
  .bar{position:absolute;top:66px;height:259px;width:11px;background:var(--band)}
  .bar--left{left:32px}
  .bar--right{left:609px}
  .bar--faint{background:rgba(0,0,0,.35)}
  .card--back .shade{position:absolute;left:0;top:325px;width:270px;height:27px;background:rgba(60,60,60,.6)}
  .brand-mark{position:absolute;left:80px;top:110px;display:flex;align-items:center;gap:10px;
    font-family:"Questrial",sans-serif;font-size:30px;color:var(--mark)}
  .brand-mark .square{width:22px;height:22px;background:var(--mark)}
  .name-box{position:absolute;left:46px;top:217px;height:56px;padding:0 10px 0 4px;background:var(--band);border-radius:0 8px 8px 0;
    font-family:"Questrial",sans-serif;font-weight:400;font-size:41px;line-height:56px;color:var(--name-grey)}
  .slogan{position:absolute;left:46px;top:288px;font-family:"Josefin Sans",sans-serif;font-weight:700;font-size:20px;color:var(--ink);letter-spacing:.3px}
  .contact{position:absolute;left:305px;top:106px;width:305px;height:193px;background:var(--panel);border-radius:10px 0 0 10px;
    font-family:"Questrial",sans-serif;font-size:21px;color:var(--panel-text)}
  .contact p{position:absolute;left:10px;white-space:nowrap}
  .contact .heading{top:12px}
  .contact .address{top:70px;left:12px}
  .contact .phone{top:112px;left:16px}
  .contact .fax{top:144px;left:18px}
  .label{position:absolute;font-family:"Josefin Sans",sans-serif;font-weight:700;font-size:21px;color:var(--label);transform:translateX(-50%)}
  .label--front{left:258px;top:423px}
  .label--back{left:849px;top:642px}
</style>
</head>
<body>
<main class="stage">
  <section class="card card--front" aria-label="Card front">
    <div class="terrazzo terrazzo--top" role="img" aria-label="Terrazzo stone texture band"></div>
    <div class="floor" role="img" aria-label="Polished concrete floor with inlaid star pattern"></div>
    <div class="band band--top"></div>
    <div class="band band--bottom"></div>
    <div class="bar bar--left"></div>
    <div class="bar bar--right"></div>
    <div class="terrazzo terrazzo--bottom" role="img" aria-label="Terrazzo stone texture band"></div>
    <div class="brand-mark"><span class="square"></span>BrightLap</div>
    <h1 class="name-box">BrightLap</h1>
    <p class="slogan">A CUT ABOVE THE REST</p>
  </section>

  <section class="card card--back" aria-label="Card back">
    <div class="terrazzo terrazzo--top" role="img" aria-label="Terrazzo stone texture band"></div>
    <div class="floor" role="img" aria-label="Polished concrete floor with inlaid star pattern"></div>
    <div class="band band--top"></div>
    <div class="band band--bottom"></div>
    <div class="shade"></div>
    <div class="bar bar--left bar--faint"></div>
    <div class="bar bar--right"></div>
    <div class="terrazzo terrazzo--bottom" role="img" aria-label="Terrazzo stone texture band"></div>
    <div class="contact">
      <p class="heading">contact info:</p>
      <p class="address">address: 14 Kiln Lane</p>
      <p class="phone">ph: 03 9412 7780</p>
      <p class="fax">fax: 03 9412 7781</p>
    </div>
  </section>

  <p class="label label--front">FRONT</p>
  <p class="label label--back">Back</p>
</main>
</body>
</html>
```